Fancy looking Inspection Postcard

Postcard needed for customers to inspect their product once it is delivered. We'll be giving them the steps for inspecting their product and to contact us if any issues arise. Would like to see something that sticks out but uses our company's colors. Would like to see creativity. Possibly utilizing the diamond steel background like we have in our logo.

Target Market(s)

Customers of our manufacturing shop

Industry/Entity Type

Manufacturing - metal wall art, custom products

Requirements
Must have
• our colors and logo
Nice to have
• get creative. i like creativity

```html
<!DOCTYPE html>
<html lang="en">
<head>
<meta charset="utf-8">
<title>Inspection Postcard</title>
<link href="https://fonts.googleapis.com/css2?family=Oswald:wght@500;600&family=Poppins:wght@400;500;600;700&display=swap" rel="stylesheet">
<style>
:root{
  --green:#6b9e3a;
  --yellow:#f7ef00;
  --ink:#1e1e1e;
  --paper:#f4f4f4;
  --page:#ffffff;
}
*{box-sizing:border-box;margin:0;padding:0}
html,body{width:772px;height:1200px;overflow:hidden;background:var(--page)}
.postcard{
  position:absolute;left:26px;top:367px;width:720px;height:466px;
  background:linear-gradient(135deg,#fafafa 0%,#ececec 45%,#f8f8f8 70%,#e9e9e9 100%);
  box-shadow:0 10px 30px rgba(0,0,0,.25);
  font-family:'Poppins',sans-serif;color:var(--ink);overflow:hidden;
}
.brand{
  position:absolute;left:25px;top:45px;width:120px;
  display:flex;flex-direction:column;align-items:center;gap:8px;
}
.brand-mark{width:26px;height:26px;border-radius:50%;background:var(--green)}
.brand-name{
  font-family:'Oswald',sans-serif;font-weight:600;font-size:19px;line-height:1.05;
  color:var(--ink);text-align:center;text-transform:uppercase;
}
.headline{
  position:absolute;left:0;top:0;width:720px;height:130px;
  font-family:'Oswald',sans-serif;font-weight:600;text-transform:uppercase;
  line-height:1;letter-spacing:-.5px;
}
.headline span{position:absolute;white-space:nowrap;transform-origin:left top}
.headline .thanks{left:173px;top:19px;font-size:47px;color:var(--ink);transform:scale(.86,1)}
.headline .inspect{left:176px;top:69px;font-size:53px;color:var(--green);transform:scale(.835,1)}
.follow{
  position:absolute;left:197px;top:140px;width:327px;height:28px;
  background:var(--ink);color:#fff;border-radius:14px;
  font-weight:700;font-size:20px;line-height:28px;text-align:center;letter-spacing:-.3px;
}
.step{position:absolute;width:340px}
.step-head{display:flex;align-items:center;gap:8px;min-height:28px}
.step-tag{border-left:3px solid var(--green);padding-left:3px;flex:none}
.step-tag span{
  display:block;background:var(--ink);color:var(--yellow);
  font-weight:700;font-size:16px;line-height:27px;padding:0 10px 0 12px;
  border-radius:0 14px 14px 0;
}
.step-title{color:var(--green);font-weight:700;font-size:15px;line-height:1.15;text-transform:uppercase}
.checklist{list-style:none;margin-top:6px}
.checklist li{display:flex;align-items:center;gap:9px;font-size:15.5px;line-height:22px;letter-spacing:.2px}
.checklist svg{flex:none;width:13px;height:13px}
.step-1{left:25px;top:184px}
.step-2{left:25px;top:272px}
.step-3{left:381px;top:184px}
.step-4{left:381px;top:272px}
.footer-band{position:absolute;left:0;top:366px;width:720px;height:100px}
.footer{position:absolute;left:0;top:372px;width:720px;height:94px;display:flex;font-weight:700}
.contact{width:374px;padding:2px 0 0 24px;border-right:1px solid var(--ink);margin:12px 0 14px}
.contact .label{font-size:12px;line-height:16px}
.contact .links{display:flex;gap:20px;color:var(--green);font-size:11.5px;font-weight:600;margin-top:2px}
.contact .links span{display:flex;align-items:center;gap:6px}
.contact .text-line{display:flex;align-items:center;gap:9px;margin-top:6px;font-size:12px}
.contact .phone{color:var(--green);font-size:21px;font-weight:600;letter-spacing:.3px}
.review{padding:16px 0 0 27px;font-size:10px;line-height:12px}
.review .reach{display:flex;align-items:baseline;gap:9px;margin-top:12px;font-size:10.5px}
.review .or{font-size:14px}
</style>
</head>
<body>
<article class="postcard">
  <div class="brand">
    <div class="brand-mark"></div>
    <div class="brand-name">Copper Ridge<br>Fabrication</div>
  </div>

  <h1 class="headline">
    <span class="thanks">Thank you for your purchase</span>
    <span class="inspect">Inspect your product now</span>
  </h1>

  <div class="follow">FOLLOW THE BELOW STEPS</div>

  <section class="step step-1">
    <div class="step-head"><div class="step-tag"><span>Step 1</span></div><h2 class="step-title">Inspect general shape</h2></div>
    <ul class="checklist">
      <li><svg viewBox="0 0 14 14"><rect x="1" y="2" width="11" height="11" fill="none" stroke="#1e1e1e" stroke-width="1.6"/><path d="M3.5 7.5l2.5 2.5 7-8" fill="none" stroke="#1e1e1e" stroke-width="1.8"/></svg>Is it what you expected?</li>
      <li><svg viewBox="0 0 14 14"><rect x="1" y="2" width="11" height="11" fill="none" stroke="#1e1e1e" stroke-width="1.6"/><path d="M3.5 7.5l2.5 2.5 7-8" fill="none" stroke="#1e1e1e" stroke-width="1.8"/></svg>Is it bent, disoriented?</li>
    </ul>
  </section>

  <section class="step step-2">
    <div class="step-head"><div class="step-tag"><span>Step 2</span></div><h2 class="step-title">Inspect the welds if<br>there are any</h2></div>
    <ul class="checklist">
      <li><svg viewBox="0 0 14 14"><rect x="1" y="2" width="11" height="11" fill="none" stroke="#1e1e1e" stroke-width="1.6"/><path d="M3.5 7.5l2.5 2.5 7-8" fill="none" stroke="#1e1e1e" stroke-width="1.8"/></svg>Do they look clean?</li>
      <li><svg viewBox="0 0 14 14"><rect x="1" y="2" width="11" height="11" fill="none" stroke="#1e1e1e" stroke-width="1.6"/><path d="M3.5 7.5l2.5 2.5 7-8" fill="none" stroke="#1e1e1e" stroke-width="1.8"/></svg>Are there any gaps?</li>
    </ul>
  </section>

  <section class="step step-3">
    <div class="step-head"><div class="step-tag"><span>Step 3</span></div><h2 class="step-title">Inspect the finish</h2></div>
    <ul class="checklist">
      <li><svg viewBox="0 0 14 14"><rect x="1" y="2" width="11" height="11" fill="none" stroke="#1e1e1e" stroke-width="1.6"/><path d="M3.5 7.5l2.5 2.5 7-8" fill="none" stroke="#1e1e1e" stroke-width="1.8"/></svg>Are there any areas not finished?</li>
      <li><svg viewBox="0 0 14 14"><rect x="1" y="2" width="11" height="11" fill="none" stroke="#1e1e1e" stroke-width="1.6"/><path d="M3.5 7.5l2.5 2.5 7-8" fill="none" stroke="#1e1e1e" stroke-width="1.8"/></svg>Are the colors what you expected?</li>
    </ul>
  </section>

  <section class="step step-4">
    <div class="step-head"><div class="step-tag"><span>Step 4</span></div><h2 class="step-title">Check for functionality</h2></div>
    <ul class="checklist">
      <li><svg viewBox="0 0 14 14"><rect x="1" y="2" width="11" height="11" fill="none" stroke="#1e1e1e" stroke-width="1.6"/><path d="M3.5 7.5l2.5 2.5 7-8" fill="none" stroke="#1e1e1e" stroke-width="1.8"/></svg>Does it work the way you want it to</li>
      <li><svg viewBox="0 0 14 14"><rect x="1" y="2" width="11" height="11" fill="none" stroke="#1e1e1e" stroke-width="1.6"/><path d="M3.5 7.5l2.5 2.5 7-8" fill="none" stroke="#1e1e1e" stroke-width="1.8"/></svg>Is it what you expected?</li>
    </ul>
  </section>

  <svg class="footer-band" viewBox="0 0 720 100" preserveAspectRatio="none">
    <path d="M0 6H588L623 16L658 6H720V100H0Z" fill="#f7ef00"/>
    <path d="M0 4H588L623 14L658 4H720" fill="none" stroke="#1e1e1e" stroke-width="4"/>
  </svg>

  <footer class="footer">
    <div class="contact">
      <div class="label">Email us at</div>
      <div class="links">
        <span><svg width="10" height="8" viewBox="0 0 10 8"><rect width="10" height="8" fill="#6b9e3a"/><path d="M0 0l5 4 5-4" fill="none" stroke="#f7ef00" stroke-width="1"/></svg>orders@crfab.com</span>
        <span><svg width="10" height="10" viewBox="0 0 10 10"><circle cx="5" cy="5" r="4.3" fill="none" stroke="#6b9e3a" stroke-width="1.2"/><path d="M.7 5h8.6M5 .7c-2.5 2.5-2.5 6.1 0 8.6M5 .7c2.5 2.5 2.5 6.1 0 8.6" fill="none" stroke="#6b9e3a" stroke-width="1"/></svg>www.crfab.com</span>
      </div>
      <div class="text-line">Shoot us a text
        <svg width="15" height="15" viewBox="0 0 24 24"><path d="M6.6 10.8a15.1 15.1 0 006.6 6.6l2.2-2.2a1 1 0 011-.25 11.4 11.4 0 003.6.6 1 1 0 011 1V20a1 1 0 01-1 1A17 17 0 013 4a1 1 0 011-1h3.5a1 1 0 011 1 11.4 11.4 0 00.6 3.6 1 1 0 01-.25 1z" fill="none" stroke="#6b9e3a" stroke-width="2"/></svg>
        <span class="phone">(208) 555-0142</span>
      </div>
    </div>
    <div class="review">
      <p>Did we do Good Job?If you think so,<br>Leave us a review on ReviewHub?If not Plese lot us know</p>
      <p class="reach"><span>info@crfab.com</span><span class="or">or</span><span>CALL US 208-555-0187</span></p>
    </div>
  </footer>
</article>
</body>
</html>
```